Business Card for beauty technology startup

Design Glowra Business Card for a Beauty, based on the website identity and colors (https://www.glowra-example.com).
Glowra is a beauty tech startup that gathers helpful product info for beauty lovers and consumers (such as availability on stores, price range and product reviews) for makeup products. The card design must be young, colorful but clean, and very modern.

Target Market(s)

woman, 15-35

Industry/Entity Type

Cosmetics

Contact Information for Business Card

Full Name, address, phone

Font styles to use
Other font styles liked:
• Advent Pro

Colors
e34297
86cfc6
ffffff
5c5c5c
e8e8e8
e667a6
b2b2b2

Requirements
Must have
• One full colored side with a creative design and another with card info
• Use Color palette: #95C5C5 and/or #D38AA5
• Use fonts: Advent Pro
• Use website identity: https://www.glowra-example.com
Nice to have
• If needed extra font: Roboto

```html
<!DOCTYPE html>
<html lang="en">
<head>
<meta charset="utf-8">
<title>Glowra Business Card</title>
<link href="https://fonts.googleapis.com/css2?family=Montserrat:wght@300;400;500;600&display=swap" rel="stylesheet">
<style>
  :root {
    --plum: #46303d;
    --rose: #b5768f;
    --paper: #ffffff;
    --ink: #4a3a44;
    --stage: #dcdcdc;
  }
  * { box-sizing: border-box; margin: 0; padding: 0; }
  html, body { width: 1200px; height: 800px; overflow: hidden; }
  body {
    background: var(--stage);
    font-family: "Montserrat", Arial, sans-serif;
    display: flex;
    align-items: center;
    justify-content: center;
    gap: 48px;
  }
  .card {
    position: relative;
    width: 520px;
    height: 297px;
    overflow: hidden;
    box-shadow: 0 4px 14px rgba(0,0,0,0.12);
  }
  /* front side */
  .card-front { background: var(--paper); color: var(--ink); }
  .name-band {
    position: absolute;
    left: 0; top: 60px;
    width: 260px; height: 58px;
    background: var(--plum);
    clip-path: polygon(0 0, 100% 0, 88% 100%, 0 100%);
    color: #fff;
    padding: 11px 0 0 26px;
  }
  .holder-name { font-size: 15px; font-weight: 600; letter-spacing: 0.5px; text-transform: uppercase; }
  .holder-role { font-size: 8.5px; font-weight: 400; letter-spacing: 0.6px; text-transform: uppercase; opacity: 0.85; margin-top: 3px; }
  .brand {
    position: absolute;
    left: 262px; top: 44px;
    display: flex; align-items: center; gap: 12px;
    color: var(--rose);
  }
  .brand-dot {
    width: 44px; height: 44px; border-radius: 50%;
    border: 2px solid var(--rose);
    background: var(--paper);
  }
  .brand-name { font-size: 30px; font-weight: 300; letter-spacing: 6px; text-transform: uppercase; }
  .address {
    position: absolute;
    right: 36px; top: 138px;
    text-align: right;
    font-size: 10.5px; line-height: 1.5; font-weight: 400;
  }
  .contacts {
    position: absolute;
    left: 40px; bottom: 30px;
    list-style: none;
    font-size: 11px; line-height: 1.55;
  }
  .contacts li { display: flex; align-items: center; gap: 9px; }
  .contacts svg { width: 9px; height: 9px; fill: none; stroke: var(--rose); stroke-width: 1.6; }
  /* back side */
  .card-back {
    background: var(--plum);
    display: flex; align-items: center; justify-content: center; gap: 16px;
    color: #fff;
  }
  .back-dot { width: 22px; height: 22px; border-radius: 50%; border: 2px solid #fff; }
  .back-name { font-size: 40px; font-weight: 300; letter-spacing: 8px; text-transform: uppercase; }
</style>
</head>
<body>
  <section class="card card-front" aria-label="Card front">
    <div class="name-band">
      <p class="holder-name">Mara Linden</p>
      <p class="holder-role">Owner</p>
    </div>
    <div class="brand">
      <span class="brand-dot"></span>
      <span class="brand-name">Glowra</span>
    </div>
    <p class="address">48 Palm Row<br>Seabrook, FL 33012</p>
    <ul class="contacts">
      <li><svg viewBox="0 0 10 10"><path d="M2 1 L4 3 L3 4.5 Q4.5 6.5 5.5 7 L7 6 L9 8 L7.5 9.3 Q2 8 0.8 2.5 Z"/></svg>555.014.2290</li>
      <li><svg viewBox="0 0 10 10"><rect x="0.8" y="2" width="8.4" height="6"/><path d="M0.8 2 L5 5.5 L9.2 2"/></svg>info@glowra-example.com</li>
      <li><svg viewBox="0 0 10 10"><circle cx="5" cy="5" r="4"/><path d="M1 5 H9 M5 1 Q2.5 5 5 9 M5 1 Q7.5 5 5 9"/></svg>www.glowra-example.com</li>
    </ul>
  </section>
  <section class="card card-back" aria-label="Card back">
    <span class="back-dot"></span>
    <span class="back-name">Glowra</span>
  </section>
</body>
</html>
```